'WILD' eye catching Business Card Design / Logo for production company / TV host / adventurer

Hi there,

We are looking for a 'WILD' and exciting logo and double sided business card for our business "Red Kettle Studios".

Corwin Baxley is an international television host, adventurer, author and inspirational public speaker.

We want to project Corwin's talents onto his business card.

We are looking for a business card design that can carry over onto letter heads, emails etc. We want a design that is 'WILD', different and exciting.

Feel free to check out Corwin's web site: www.redkettlestudios.co.nz to get a better understanding what he is about.

Please feel free to go completely 'WILD' on this project as we want something different with lots of WOW factors.

Thank you so much and we look forward to your designs.

We have a feeling that there will be many more designs in the near future.

Best regards,

the production team

We have added another task to the list.

If the winning designer can also provide us with a matching letterhead and email signature based on the same style of design as the business card.

Target Market(s)

People with passion.

Industry/Entity Type

Business

Requirements
Must have
• Red Kettle Studios
Corwin Baxley
42 Fernhill Lane
Ashbury 7388
New Zealand

Phone +64-(0)3-5027 416
Cell +64-(0)274-861 052

email: redkettlenz@mailbox-example.nz
www.redkettlestuios.co.nz
Nice to have
• A feature made out of the name 'Red Kettle Studios'.

Corwin Baxley's name reasonably obvious.

All other details (except web site) can be quite small.

```html
<!DOCTYPE html>
<html lang="en">
<head>
<meta charset="utf-8">
<title>Red Kettle Studios – Business Card Backs</title>
<link rel="stylesheet" href="https://fonts.googleapis.com/css2?family=Patrick+Hand&family=Poppins:wght@800&display=swap">
<style>
  :root {
    --sand-light: #efc48e;
    --sand-mid: #e2ab6f;
    --sand-dark: #d0955a;
    --card-bg: #fcf2a4;
    --ink-brown: #6b3411;
    --ink-dark: #4b3a2c;
    --logo-brown: #7a3f16;
    --label-white: #ffffff;
  }
  * { margin: 0; padding: 0; box-sizing: border-box; }
  html, body { width: 1200px; height: 675px; overflow: hidden; }
  body { position: relative; font-family: "Patrick Hand", cursive; }

  .sand-backdrop {
    position: absolute; inset: 0;
    background:
      linear-gradient(160deg, rgba(255,255,255,0.12) 0%, rgba(0,0,0,0) 40%, rgba(0,0,0,0.08) 100%),
      linear-gradient(180deg, var(--sand-light) 0%, var(--sand-mid) 55%, var(--sand-dark) 100%);
  }

  .brand-title {
    position: absolute; left: 0; top: 22px; width: 1200px;
    text-align: center; color: var(--logo-brown);
    font-family: "Patrick Hand", cursive; line-height: 1;
  }
  .brand-title .line-main { display: block; font-size: 104px; letter-spacing: 4px; }
  .brand-title .line-sub { display: block; font-size: 72px; letter-spacing: 10px; margin-top: -4px; }

  .card-strip {
    position: absolute; left: 48px; top: 234px; width: 1070px; height: 218px;
    background: var(--card-bg);
  }
  .card { position: absolute; top: 0; width: 356px; height: 218px; color: var(--ink-dark); }
  .card--plain { left: 0; }
  .card--logo { left: 356px; }
  .card--strip { left: 712px; }

  .card-name { position: absolute; font-size: 29px; color: var(--ink-brown); white-space: nowrap; }
  .card-url { position: absolute; left: 0; width: 100%; text-align: center; font-size: 23px; color: var(--ink-dark); white-space: nowrap; }
  .card-address, .card-contact { position: absolute; font-size: 14px; line-height: 15px; white-space: nowrap; }
  .card-contact { text-align: right; }

  .card-mark {
    position: absolute; text-align: center; color: var(--logo-brown);
    font-family: "Patrick Hand", cursive; line-height: 1;
  }
  .card-mark span { display: block; }
  .card-mark .mark-main { font-size: 22px; letter-spacing: 1px; }
  .card-mark .mark-sub { font-size: 15px; letter-spacing: 2px; }

  .card--plain .card-name { left: 105px; top: 42px; }
  .card--plain .card-url { top: 92px; }
  .card--plain .card-address { left: 17px; top: 155px; }
  .card--plain .card-contact { right: 15px; top: 155px; }

  .card--logo .card-name { left: 17px; top: 32px; }
  .card--logo .card-mark { right: 12px; top: 30px; }
  .card--logo .card-url { top: 92px; }
  .card--logo .card-address { left: 17px; top: 155px; }
  .card--logo .card-contact { right: 14px; top: 155px; }

  .card--strip .card-name { left: 66px; top: 18px; }
  .card--strip .card-mark { right: 16px; top: 17px; }
  .card--strip .card-url { top: 76px; }
  .card--strip .card-address { left: 66px; top: 133px; }
  .card--strip .card-contact { right: 16px; top: 133px; }
  .card-textures {
    position: absolute; left: 50px; right: 0; bottom: 0; height: 28px;
    background: linear-gradient(90deg, #c9731f 0%, #2f9dba 20%, #8b7a3a 38%, #bdbdb8 55%, #4f9a2c 72%, #c85a1a 100%);
  }

  .side-label {
    position: absolute; top: 472px; width: 300px; text-align: center;
    font-family: "Poppins", sans-serif; font-weight: 800; font-size: 42px;
    letter-spacing: 2px; color: var(--label-white);
  }
  .side-label--1 { left: 66px; }
  .side-label--2 { left: 452px; }
  .side-label--3 { left: 811px; }
</style>
</head>
<body>
  <div class="sand-backdrop" role="img" aria-label="Rippled desert sand texture"></div>

  <h1 class="brand-title">
    <span class="line-main">Red Kettle</span>
    <span class="line-sub">Studios</span>
  </h1>

  <section class="card-strip">
    <article class="card card--plain">
      <p class="card-name">Corwin Baxley</p>
      <p class="card-url">www.redkettlestudios.co.nz</p>
      <p class="card-address">42 Fernhill Lane<br>Ashbury 7388<br>New Zealand</p>
      <p class="card-contact">+64-(0)3-5027 416<br>+64-(0)274-861 052<br>redkettlenz@mailbox-example.nz</p>
    </article>

    <article class="card card--logo">
      <p class="card-name">Corwin Baxley</p>
      <p class="card-mark"><span class="mark-main">Red Kettle</span><span class="mark-sub">Studios</span></p>
      <p class="card-url">www.redkettlestudios.co.nz</p>
      <p class="card-address">42 Fernhill Lane<br>Ashbury 7388<br>New Zealand</p>
      <p class="card-contact">+64-(0)3-5027 416<br>+64-(0)274-861 052<br>redkettlenz@mailbox-example.nz</p>
    </article>

    <article class="card card--strip">
      <p class="card-name">Corwin Baxley</p>
      <p class="card-mark"><span class="mark-main">Red Kettle</span><span class="mark-sub">Studios</span></p>
      <p class="card-url">www.redkettlestudios.co.nz</p>
      <p class="card-address">42 Fernhill Lane<br>Ashbury 7388<br>New Zealand</p>
      <p class="card-contact">+64-(0)3-5027 416<br>+64-(0)274-861 052<br>redkettlenz@mailbox-example.nz</p>
      <div class="card-textures" role="img" aria-label="Row of wild textures: tiger fur, water, reptile skin, zebra stripes, green leaf and orange fur"></div>
    </article>
  </section>

  <p class="side-label side-label--1">BACK</p>
  <p class="side-label side-label--2">BACK</p>
  <p class="side-label side-label--3">BACK</p>
</body>
</html>
```